TIKLOOMTOT WEBSITE DESIGN

We need a website design based on the template- http://varolapixels.com/themes/quartzpage-bootstrap-wordpress-theme/. We purchased template and will build the website using wordpress. It is one page application. We wanted to list all content in one page and make it browser friendly (can be viewed in cell phone, pc, mac, ipad, etc).

The target audience is parents with babies/kids age from 0-5 year old. We wanted to sell the subscription based monthly boxes to the families. The box will include books, toys, crafts, kids consumer products and letter/note/card to the family from the experts. All boxes are customized based on children's age, gender and interests.

We wanted the site main color to be blue.

Please refer to these websites for ideas.
froxi.com
wwws.pebbleharbor.com
http://www.wigglyoats.com/

I've updated the project brief and make the project fund guaranteed. Thanks!

Target Market(s)

Parents with kids age from 0-5 years old. Mainly target to the China market.

Industry/Entity Type

Cell Phone

Colors
3277b5
85abd2
85cae6
33a6d7
0592cd
0355a3
ceddec
cee9f5

Requirements
Must have
• Must provide the design based on the template- http://varolapixels.com/themes/quartzpage-bootstrap-wordpress-theme/.
The site has to be Chinese character friendly since we are going to post Chinese content on the website. No English content.
The registration forms needs to be designed and include in the final deliverable.

```html
<!DOCTYPE html>
<html lang="zh">
<head>
<meta charset="utf-8">
<title>TIKLOOMTOT</title>
<link rel="stylesheet" href="https://fonts.googleapis.com/css2?family=Tinos&family=Noto+Sans+SC:wght@400&display=swap">
<style>
:root{
  --header:#3277b5;
  --deep:#0355a3;
  --sky:#85cae6;
  --pale:#ceddec;
  --mist:#cee9f5;
  --muted:#85abd2;
  --white:#ffffff;
}
*{margin:0;padding:0;box-sizing:border-box}
html,body{width:1060px;height:1200px;overflow:hidden}
body{position:relative;background:var(--deep);font-family:"Tinos",serif;color:var(--header)}
.abs{position:absolute}
.site-header{left:0;top:0;width:1060px;height:110px;background:var(--header)}
.header-band{left:0;top:110px;width:1060px;height:24px;background:var(--deep)}
.brand-mark{left:113px;top:13px;width:82px;height:82px;border-radius:50%;background:var(--pale);border:3px solid var(--deep)}
.brand-name{left:222px;top:49px;font-size:15px;color:var(--muted)}
.brand-cn{left:222px;top:67px;font-size:16px;color:var(--white);font-family:"Noto Sans SC",sans-serif}
.nav{top:59px;font-size:16px;color:var(--white)}
.nav-icon{left:927px;top:61px;width:22px;height:22px;border-radius:50%;background:var(--pale)}
.about{left:0;top:134px;width:1060px;height:769px;background:var(--sky)}
.section-title{font-size:30px;font-weight:400;color:var(--header)}
.about-text{left:112px;top:205px;width:840px;font-family:"Noto Sans SC",sans-serif;font-size:12.5px;line-height:16.5px;color:var(--header)}
.photo{border:4px solid var(--pale)}
.photo-pink{background:linear-gradient(135deg,#f3cbd6,#e8e2d8 55%,#7aa86a)}
.photo-blue{background:linear-gradient(135deg,#8a5a46,#d9cdb3 45%,#b7cfe6)}
.photo-box{background:linear-gradient(135deg,#b9d0ea,#ece8df 55%,#c9a552)}
.dots{top:578px;display:flex;gap:4px}
.dots span{width:5px;height:5px;background:var(--header)}
.dots span.on{background:var(--mist)}
.advisor{top:647px;width:201px;height:202px;border:4px solid var(--header);background:linear-gradient(160deg,#c9d6c4,#b79c86 60%,#6b7b8a)}
.advisor-name{top:857px;width:201px;text-align:center;font-size:15px;color:var(--header)}
.order-title{left:547px;top:1017px;color:var(--pale)}
.field{height:33px;background:var(--header);border:3px solid var(--pale);color:var(--white);font-size:14px;padding:3px 0 0 12px}
</style>
</head>
<body>
<header class="abs site-header"></header>
<div class="abs header-band"></div>
<div class="abs brand-mark"></div>
<div class="abs brand-name">tikloomtot</div>
<div class="abs brand-cn">美国童趣宝盒俱乐部</div>
<nav>
  <span class="abs nav" style="left:545px">About us</span>
  <span class="abs nav" style="left:625px">Our advisors</span>
  <span class="abs nav" style="left:731px">Order now</span>
  <span class="abs nav" style="left:823px">FAQ</span>
  <span class="abs nav" style="left:871px">Blog</span>
  <span class="abs nav-icon"></span>
</nav>

<section class="abs about"></section>
<h2 class="abs section-title" style="left:112px;top:154px">About us</h2>
<p class="abs about-text">美国童趣宝盒俱乐部 ——让孩子足不出户，享受美国最先进的早期教育和育儿理念的平台。<br>
加入我们的每月神秘礼包，爸爸妈妈和宝宝即可获得美国专家推荐的美国原版婴幼儿书籍及专家心得，培养孩子良好的生活习惯的日常用品，以及最新的婴幼儿智力开发玩具手工。爸爸妈妈也会收获双倍的惊喜。<br>
与美国权威育儿专家进行1对1的交流，用科学、个性化的育儿理念、书籍和物品帮助宝宝健康、快乐的成长。</p>

<div class="abs photo photo-pink" style="left:110px;top:302px;width:415px;height:265px" role="img" aria-label="粉色小熊与玩具礼盒"></div>
<div class="abs photo photo-blue" style="left:535px;top:302px;width:414px;height:265px" role="img" aria-label="猴子背包与蓝色小熊"></div>
<div class="abs dots" style="left:293px"><span></span><span></span><span></span><span class="on"></span><span></span></div>
<div class="abs dots" style="left:718px"><span></span><span class="on"></span><span></span><span></span><span></span></div>

<h2 class="abs section-title" style="left:111px;top:598px">Our advisors</h2>
<div class="abs advisor" style="left:108px" role="img" aria-label="顾问照片一"></div>
<div class="abs advisor" style="left:323px" role="img" aria-label="顾问照片二"></div>
<div class="abs advisor" style="left:535px" role="img" aria-label="顾问照片三"></div>
<div class="abs advisor" style="left:748px" role="img" aria-label="顾问照片四"></div>
<div class="abs advisor-name" style="left:108px">Expert 1</div>
<div class="abs advisor-name" style="left:323px">Expert 2</div>
<div class="abs advisor-name" style="left:535px">Expert 3</div>
<div class="abs advisor-name" style="left:748px">Expert 4</div>

<div class="abs photo photo-box" style="left:111px;top:1024px;width:402px;height:200px" role="img" aria-label="蓝色小熊与蜡笔礼盒"></div>
<h2 class="abs section-title order-title">Order now</h2>
<form>
  <div class="abs field" style="left:547px;top:1075px;width:200px">Name</div>
  <div class="abs field" style="left:758px;top:1075px;width:191px">Surname</div>
  <div class="abs field" style="left:547px;top:1124px;width:402px">Address</div>
  <div class="abs field" style="left:547px;top:1172px;width:402px">City</div>
</form>
</body>
</html>
```